Voltren Assemblies, Inc. Business Card

Voltren has three operating entities and I'm looking for a standard business card template that can be used for Voltren and the three operating entities that the logo just get swapped out, but has a very similar look and feel. Ultimately if someone had a business card from each, they assume the organizations are related because they all have the same look and feel.
Below are our websites and I will attached the logos for each entity:
https://www.voltrenassemblies-example.com/
https://www.brackwayceramic-example.com/
https://www.omdr-pqsx-example.com/
https://www.tamberlinebreaker-example.com/

Target Market(s)

US Voltren

Industry/Entity Type

US Voltren

Contact Information for Business Card

Normal stuff

```html
<!DOCTYPE html>
<html lang="en">
<head>
<meta charset="utf-8">
<title>Voltren Assemblies, Inc. — Business Card</title>
<link href="https://fonts.googleapis.com/css2?family=Montserrat:wght@600;700&family=Open+Sans:wght@400&display=swap" rel="stylesheet">
<style>
  :root {
    --stage: #141518;
    --navy: #2a3570;
    --navy-light: #3a4682;
    --red: #c8202f;
    --white: #ffffff;
    --grey-text: #5f6068;
    --rule: #4a4f86;
  }
  * { margin: 0; padding: 0; box-sizing: border-box; }
  html, body {
    width: 1200px; height: 848px; overflow: hidden;
    background: var(--stage);
  }
  .canvas { position: relative; width: 1200px; height: 848px; }

  .card {
    position: absolute; top: 294px;
    width: 434px; height: 260px;
    box-shadow: 0 10px 24px rgba(0,0,0,.55);
    overflow: hidden;
  }
  .card--front { left: 144px; }
  .card--back { left: 622px; background: var(--white); }

  .front-scene {
    position: absolute; inset: 0;
    background: linear-gradient(180deg, var(--navy) 0%, var(--navy) 35%, var(--navy-light) 78%, var(--navy) 100%);
  }
  .front-brand {
    position: absolute; left: 77px; top: 104px;
    display: flex; align-items: center; gap: 14px;
  }
  .brand-dot { width: 48px; height: 48px; border-radius: 50%; flex: none; }
  .front-brand .brand-dot { background: var(--white); }
  .brand-name {
    font-family: "Montserrat", sans-serif; font-weight: 700;
    white-space: nowrap; letter-spacing: .2px;
  }
  .front-brand .brand-name { color: var(--white); font-size: 19px; }

  .back-brand {
    position: absolute; left: 0; right: 0; top: 38px;
    display: flex; flex-direction: column; align-items: center; gap: 12px;
  }
  .back-brand .brand-dot { width: 60px; height: 60px; background: var(--navy); }
  .back-brand .brand-name { color: var(--navy); font-size: 19px; }

  .rule { position: absolute; left: 65px; width: 304px; height: 1px; background: var(--rule); }
  .rule--top { top: 153px; }
  .rule--bottom { top: 208px; }

  .person {
    position: absolute; right: 273px; top: 160px; text-align: right;
  }
  .person-name {
    font-family: "Montserrat", sans-serif; font-weight: 600;
    font-size: 16px; color: var(--navy); line-height: 20px; white-space: nowrap;
  }
  .person-title {
    font-family: "Open Sans", sans-serif; font-size: 11px;
    color: var(--grey-text); line-height: 14px;
  }

  .contacts { position: absolute; left: 171px; top: 156px; list-style: none; }
  .contacts li {
    display: flex; align-items: center; gap: 5px; height: 16.5px;
    font-family: "Open Sans", sans-serif; font-size: 11.5px; color: var(--grey-text);
    white-space: nowrap;
  }
  .contacts svg { width: 9px; height: 9px; flex: none; }

  .address {
    position: absolute; left: 0; right: 0; top: 213px; text-align: center;
    font-family: "Open Sans", sans-serif; font-size: 11.5px; color: var(--grey-text);
  }
</style>
</head>
<body>
<div class="canvas">

  <section class="card card--front">
    <div class="front-scene" role="img" aria-label="Photograph of electrical transmission towers and power lines in navy blue tint"></div>
    <div class="front-brand">
      <span class="brand-dot"></span>
      <span class="brand-name">Voltren Assemblies, Inc.</span>
    </div>
  </section>

  <section class="card card--back">
    <div class="back-brand">
      <span class="brand-dot"></span>
      <span class="brand-name">Voltren Assemblies, Inc.</span>
    </div>

    <div class="rule rule--top"></div>

    <div class="person">
      <p class="person-name">Dana Merrow</p>
      <p class="person-title">Sales Manager</p>
    </div>

    <ul class="contacts">
      <li>
        <svg viewBox="0 0 10 10" aria-hidden="true"><circle cx="5" cy="5" r="5" fill="#c8202f"/><path d="M3.2 2.6l1 1-.5.6c.4.8.9 1.3 1.6 1.6l.6-.5 1 1-.6.8c-1.8-.3-3.1-1.6-3.5-3.5z" fill="#fff"/></svg>
        02 5550 0142
      </li>
      <li>
        <svg viewBox="0 0 10 10" aria-hidden="true"><circle cx="5" cy="5" r="5" fill="#c8202f"/><rect x="2.6" y="3.3" width="4.8" height="3.4" fill="none" stroke="#fff" stroke-width=".7"/><path d="M2.6 3.3L5 5.2l2.4-1.9" fill="none" stroke="#fff" stroke-width=".7"/></svg>
        mail@voltren-example.com
      </li>
      <li>
        <svg viewBox="0 0 10 10" aria-hidden="true"><circle cx="5" cy="5" r="5" fill="#c8202f"/><circle cx="5" cy="5" r="2.7" fill="none" stroke="#fff" stroke-width=".6"/><path d="M2.3 5h5.4M5 2.3v5.4" stroke="#fff" stroke-width=".5"/></svg>
        www.voltrenassemblies-example.com
      </li>
    </ul>

    <div class="rule rule--bottom"></div>

    <p class="address">118 W Harlow Rd, Suite 2 Fenmoor, OH 40000</p>
  </section>

</div>
</body>
</html>
```